Counseling Practice Business Card

I need a professional looking business card incorporating my new logo that was just completed. Card needs to incorporate my name and title, description of my specialty, my address, my phone number, my fax number, my email and my website URL. I need to be able to choose design on/with different paper colors and textures.
I do not have a lot of business card ideas so I am open to anything but I want bold,sharp, clear card without additional designs other than my logo (see attached file info). I am open to different color backgrounds or paper colors including black. I do not like traditional brackets around area codes in phone number or dashes between numbers in phone number. Am open to other ways of presenting including periods between numbers as appropriate. I do not know enough to know what I like yet but I want card to coordinate and work together with my logo. My practice emphasizes natural mental health interventions so any use of color (with background paper color or the blue and green in my logo) that elicits nature is nice. In addition to black, any natural brown or wood looking background might be desirable also. Most of the offerings so far look very similar and boring.

Target Market(s)

Potential therapy clients and other professionals

Contact Information for Business Card

Card information:
Marcus T. Whitfield, Ph.D.
Licensed Clinical Psychologist
Integrative Health Coach
4812 Ferndale Pkwy NW
Suite 730
Duluth, GA 30096
(770) 555-0142 phone
(770) 555-0186 fax
drmarcuswhitfield@kelvora.com
pathbloomcounseling.com

Font styles to use
Serif
Sans Serif
Other font styles liked:
• anything that you think looks crisp, clear and easily readable

Requirements
Must have
• Any color used should coordinate with my logo design (see attached files).
• Card should be printed horizontally so top and bottom are longest sides of rectangle.
• Background color or paper color should complement and highlight logo. Do not like a white background. black, grey, brown or any color my logo would blend well with.
Nice to have
• I would like designer to utilize color to highlight letters/name or phone-fax-web symbols.
• Bottom edge of card could be highlighted if appropriate to an idea.
Should not have
• I would NOT want the card to have a pure white background at all.
• No clear cards.
• Cards should be oriented with long sides on bottom and top, NOT sides. DO NOT LIKE THIS THIN TALL ORIENTATION.

```html
<!DOCTYPE html>
<html lang="en">
<head>
<meta charset="utf-8">
<title>Pathbloom Counseling – Business Card</title>
<link rel="stylesheet" href="https://fonts.googleapis.com/css2?family=Montserrat:wght@400;500;700&family=Lato:wght@300;400&display=swap">
<style>
  :root {
    --bg: #3a3c3f;
    --card: #141414;
    --brand-blue: #1a8fd6;
    --text-white: #f2f2f2;
    --text-grey: #b9b9b9;
    --divider-shadow: #050505;
  }
  * { margin: 0; padding: 0; box-sizing: border-box; }
  html, body { width: 1200px; height: 1200px; overflow: hidden; }
  body {
    background: var(--bg);
    font-family: "Montserrat", sans-serif;
    position: relative;
  }
  .card {
    position: absolute;
    left: 140px;
    width: 920px;
    height: 526px;
    background: var(--card);
    border-radius: 40px;
    overflow: hidden;
  }
  .card--back { top: 50px; }
  .card--front { top: 624px; }

  .wordmark {
    position: absolute;
    color: var(--brand-blue);
    font-family: "Montserrat", sans-serif;
    font-weight: 500;
    text-align: center;
    line-height: 1;
  }
  .wordmark__name { display: block; font-size: 70px; letter-spacing: -1px; }
  .wordmark__tag { display: block; font-size: 24px; letter-spacing: 14px; margin-top: 10px; padding-left: 14px; }

  .card--back .wordmark { left: 0; right: 0; top: 170px; }
  .back-url {
    position: absolute;
    top: 372px;
    left: 0; right: 0;
    text-align: center;
    color: var(--brand-blue);
    font-family: "Lato", sans-serif;
    font-size: 22px;
    letter-spacing: 0.5px;
  }
  .back-rule {
    position: absolute;
    height: 1px;
    background: var(--brand-blue);
  }
  .back-rule--left { left: 0; width: 318px; top: 386px; }
  .back-rule--right { right: 0; width: 200px; top: 262px; }

  .card--front .wordmark { left: 40px; width: 400px; top: 190px; }
  .card--front .wordmark__name { font-size: 62px; }
  .card--front .wordmark__tag { font-size: 22px; letter-spacing: 12px; }

  .front-divider {
    position: absolute;
    left: 470px; top: 80px;
    width: 4px; height: 366px;
    background: var(--divider-shadow);
    box-shadow: 2px 0 6px rgba(0,0,0,0.7);
  }
  .profile {
    position: absolute;
    left: 500px; top: 78px;
  }
  .profile__name {
    color: var(--brand-blue);
    font-weight: 700;
    font-size: 25px;
    letter-spacing: -0.3px;
  }
  .profile__role {
    color: var(--text-grey);
    font-family: "Lato", sans-serif;
    font-weight: 300;
    font-size: 19px;
    line-height: 1.3;
  }
  .contacts {
    position: absolute;
    left: 474px; top: 196px;
    list-style: none;
  }
  .contact {
    display: flex;
    align-items: center;
    height: 58px;
  }
  .contact__tab {
    width: 36px; height: 16px;
    background: var(--brand-blue);
  }
  .contact__icon {
    width: 42px; height: 42px;
    border-radius: 50%;
    border: 3px solid var(--brand-blue);
    background: var(--card);
    margin-left: -6px;
    display: flex; align-items: center; justify-content: center;
  }
  .contact__icon svg { width: 20px; height: 20px; }
  .contact__text {
    margin-left: 14px;
    color: var(--text-white);
    font-size: 17px;
    line-height: 1.25;
  }
</style>
</head>
<body>

<section class="card card--back">
  <div class="wordmark">
    <span class="wordmark__name">Pathbloom</span>
    <span class="wordmark__tag">COUNSELING</span>
  </div>
  <div class="back-rule back-rule--right"></div>
  <div class="back-rule back-rule--left"></div>
  <p class="back-url">www.pathbloomcounseling.com</p>
</section>

<section class="card card--front">
  <div class="wordmark">
    <span class="wordmark__name">Pathbloom</span>
    <span class="wordmark__tag">COUNSELING</span>
  </div>

  <div class="front-divider"></div>

  <div class="profile">
    <h1 class="profile__name">MARCUS T. WHITFIELD Ph.D</h1>
    <p class="profile__role">Licensed Clinical Psychologist</p>
    <p class="profile__role">Integrative Health Coach</p>
  </div>

  <ul class="contacts">
    <li class="contact">
      <span class="contact__tab"></span>
      <span class="contact__icon">
        <svg viewBox="0 0 24 24" fill="#fff"><path d="M3 9c0-3 4-5 9-5s9 2 9 5v2h-5V9c-1-1-7-1-8 0v2H3z"/><rect x="5" y="12" width="14" height="8" rx="1.5"/><circle cx="12" cy="16" r="2" fill="#141414"/></svg>
      </span>
      <span class="contact__text">+770 . 555 . 0142<br>+770 . 555 . 0186</span>
    </li>
    <li class="contact">
      <span class="contact__tab"></span>
      <span class="contact__icon">
        <svg viewBox="0 0 24 24"><rect x="3" y="6" width="18" height="12" fill="#fff"/><path d="M3 6l9 7 9-7M3 18l7-6M21 18l-7-6" stroke="#141414" stroke-width="1.5" fill="none"/></svg>
      </span>
      <span class="contact__text">drmarcuswhitfield@kelvora.com</span>
    </li>
    <li class="contact">
      <span class="contact__tab"></span>
      <span class="contact__icon">
        <svg viewBox="0 0 24 24" fill="none" stroke="#fff" stroke-width="1.6"><circle cx="12" cy="12" r="9"/><ellipse cx="12" cy="12" rx="4" ry="9"/><path d="M3 12h18M5 7h14M5 17h14"/></svg>
      </span>
      <span class="contact__text">www.pathbloomcounseling.com</span>
    </li>
    <li class="contact">
      <span class="contact__tab"></span>
      <span class="contact__icon">
        <svg viewBox="0 0 24 24" fill="#fff"><path d="M12 3l10 9h-3v8h-5v-5h-4v5H5v-8H2z"/></svg>
      </span>
      <span class="contact__text">4812 Ferndale Pkwy NW<br>Suite 730, Duluth, GA 30096</span>
    </li>
  </ul>
</section>

</body>
</html>
```